business card with 2 locations on 1 card

I need a modern looking business card that I would use at 2 different locations. Possibly 1 location on 1 side and other location on other side. One should be able to distinguish the 2 locations immediately before having to read the address or description on card. You can take a look at my website to see what I'm drawn to. The logo is brand new that I just purchased on Craft Hive. I want to emphasize family.
Updates

Let's not use the yellow and blue colors. Added Thursday, August 31, 2017

Target Market(s)

women and children

Industry/Entity Type

Health And Wellness

Contact Information for Business Card

Business name: Willow Brook Chiropractic & Acupuncture
My name: Lorin Daske
Job title: DC, MSOM, LAc (NM), CCN

Location 1
Address: 4817 Marlowe Blvd, Suite C-240, Ashmere, TX 75091
Phone: (469) 555-0182
Fax: (972) 555-0137

Location 2
Address: 1936 Belvane Road, Suite 310, Hollin Park, TX 75062
Phone: (469) 555-0169
Fax: (972) 555-0137

Email: drlorindaske@mailnest.example
Website: www.drlorindaske.example

Font styles to use
Serif
Sans Serif

Colors

Designer to choose colors to be used in the design.

Requirements
Must have
• distinction between 2 locations.
Nice to have
• Colors preference below is there. But I like to see what you come up with too!

```html
<!DOCTYPE html>
<html lang="en">
<head>
<meta charset="utf-8">
<title>Willow Brook Chiropractic &amp; Acupuncture – Business Cards</title>
<link rel="stylesheet" href="https://fonts.googleapis.com/css2?family=EB+Garamond:wght@400;500;600&display=swap">
<style>
  :root {
    --teal: #3a616e;
    --teal-deep: #2f6b68;
    --paper: #f3f3f3;
    --white: #ffffff;
    --backdrop: #ececec;
    --text-font: "EB Garamond", Garamond, serif;
  }
  * { box-sizing: border-box; margin: 0; padding: 0; }
  html, body { width: 1200px; height: 586px; overflow: hidden; }
  body { background: var(--backdrop); font-family: var(--text-font); position: relative; }

  .card { position: absolute; top: 129px; width: 501px; height: 300px; overflow: hidden; background: var(--teal); }
  .card--north { left: 61px; }
  .card--south { left: 619px; }

  .brand-panel { position: absolute; left: 0; top: 0; width: 256px; height: 100%; background: var(--paper); }
  .stripe { position: absolute; top: 0; width: 3px; height: 100%; background: var(--white); }
  .stripe--a { left: 259px; }
  .stripe--b { left: 265px; }

  .brand { position: absolute; width: 240px; text-align: center; }
  .brand-ring { display: block; margin: 0 auto; width: 101px; height: 101px; border-radius: 50%; border: 5px solid currentColor; }
  .brand-name { font-weight: 500; text-transform: uppercase; margin-top: 14px; }
  .brand-name .line1 { display: block; font-size: 23px; line-height: 1; letter-spacing: 0.4px; }
  .brand-name .line2 { display: block; font-size: 10px; line-height: 1.2; letter-spacing: 0.4px; margin-top: 2px; }
  .card--north .brand { left: 8px; top: 71px; color: var(--teal-deep); }
  .card--south .brand { left: 249px; top: 71px; color: var(--white); }

  .details { position: absolute; color: var(--white); font-size: 11.5px; line-height: 1.5; }
  .card--north .details { left: 298px; top: 90px; }
  .card--south .details { left: 38px; top: 93px; }

  .person-name { font-size: 16px; font-weight: 600; line-height: 1.2; }
  .credentials { font-size: 11px; margin-top: 4px; }
  .web { font-size: 11px; font-weight: 400; line-height: 1.55; }

  .contact-list { list-style: none; margin-top: 28px; }
  .card--south .contact-list { margin-top: 20px; }
  .contact-list li { display: flex; align-items: center; gap: 8px; height: 16px; margin-bottom: 9px; }
  .icon { width: 16px; height: 16px; flex: none; }
  .address { margin-top: 2px; line-height: 1.55; }
</style>
</head>
<body>

<section class="card card--north" aria-label="Ashmere location card">
  <div class="brand-panel"></div>
  <div class="stripe stripe--a"></div>
  <div class="stripe stripe--b"></div>

  <div class="brand">
    <span class="brand-ring"></span>
    <p class="brand-name"><span class="line1">Willow Brook</span><span class="line2">Chiropractic &amp; Acupuncture</span></p>
  </div>

  <div class="details">
    <p class="person-name">Lorin Daske</p>
    <p class="credentials">DC, MSOM, LAc (NM), CCN</p>
    <ul class="contact-list">
      <li>
        <svg class="icon" viewBox="0 0 16 16" aria-hidden="true"><circle cx="8" cy="8" r="8" fill="#fff"/><path d="M4 9.5h8l-1-3H5z M6 6.5V5h4v1.5" fill="none" stroke="#3a616e" stroke-width="1.2"/><rect x="4" y="9.5" width="8" height="2" fill="#3a616e"/></svg>
        <span>(469) 555-0182</span>
      </li>
      <li>
        <svg class="icon" viewBox="0 0 16 16" aria-hidden="true"><circle cx="8" cy="8" r="8" fill="#fff"/><rect x="4" y="5" width="8" height="6" fill="none" stroke="#3a616e" stroke-width="1.2"/><path d="M4 5l4 3.5L12 5" fill="none" stroke="#3a616e" stroke-width="1.2"/></svg>
        <span>(972) 555-0137</span>
      </li>
    </ul>
    <p class="address">4817 Marlowe Blvd,<br>Suite C-240, Ashmere, TX 75091</p>
  </div>
</section>

<section class="card card--south" aria-label="Hollin Park location card">
  <div class="details">
    <p class="web">drlorindaske@mailnest.example<br>www.drlorindaske.example</p>
    <ul class="contact-list">
      <li>
        <svg class="icon" viewBox="0 0 16 16" aria-hidden="true"><circle cx="8" cy="8" r="8" fill="#fff"/><path d="M4 9.5h8l-1-3H5z M6 6.5V5h4v1.5" fill="none" stroke="#3a616e" stroke-width="1.2"/><rect x="4" y="9.5" width="8" height="2" fill="#3a616e"/></svg>
        <span>(469) 555-0169</span>
      </li>
      <li>
        <svg class="icon" viewBox="0 0 16 16" aria-hidden="true"><circle cx="8" cy="8" r="8" fill="#fff"/><rect x="4" y="5" width="8" height="6" fill="none" stroke="#3a616e" stroke-width="1.2"/><path d="M4 5l4 3.5L12 5" fill="none" stroke="#3a616e" stroke-width="1.2"/></svg>
        <span>(972) 555-0137</span>
      </li>
    </ul>
    <p class="address">1936 Belvane Road,<br>Suite 310, Hollin Park, TX 75062</p>
  </div>

  <div class="brand">
    <span class="brand-ring"></span>
    <p class="brand-name"><span class="line1">Willow Brook</span><span class="line2">Chiropractic &amp; Acupuncture</span></p>
  </div>
</section>

</body>
</html>
```